Commercial Broker Profile Flyer

I need a one-page flyer created that will serve as a profile report for individual brokers within a commercial real estate firm. The flyer will include company branding, agent photo, bio, and other information. I would like to have the source file available for future editing preferably in a Publisher file format. A copy of a company brochure is included and would like to have this profile flyer similar to keep company branding consistent. Our company website is www.coltbrinwellre.com for any other questions on branding.

Target Market(s)

Professional

Industry/Entity Type

Real Estate Agent

Requirements
Must have
• One page
• Source files MUST include a .PUB file that I can update in the future
• All of the information in the uploaded "content" file
• Company branding
• Must be 8.5"x11"
Should not have
• Do not use stock photos or property photos from the attachments. I only want the broker photo and company logo.

```html
<!DOCTYPE html>
<html lang="en">
<head>
<meta charset="utf-8">
<title>Broker Profile – R. Dalton Brinwell</title>
<link rel="stylesheet" href="https://fonts.googleapis.com/css2?family=Encode+Sans:wght@300;400;500&family=Encode+Sans+Semi+Condensed:wght@300;500&display=swap">
<style>
  :root {
    --brand-green: #0b6b3f;
    --brand-green-dark: #075a34;
    --ink: #222;
    --paper: #fff;
    --wave-mint: #cdeedd;
    --wave-lime: #eef6c8;
  }
  * { box-sizing: border-box; margin: 0; padding: 0; }
  html, body { width: 848px; height: 1200px; overflow: hidden; background: var(--paper); }
  body { font-family: "Encode Sans", sans-serif; font-weight: 300; color: var(--ink); }
  .page { position: relative; width: 848px; height: 1200px; overflow: hidden; }

  .backdrop-wave {
    position: absolute; left: 0; right: 0; bottom: 0; height: 340px;
    background:
      radial-gradient(ellipse 70% 45% at 30% 75%, var(--wave-mint) 0%, rgba(205,238,221,0) 70%),
      radial-gradient(ellipse 60% 55% at 85% 40%, var(--wave-lime) 0%, rgba(238,246,200,0) 70%),
      linear-gradient(180deg, rgba(255,255,255,0) 0%, rgba(230,245,225,0.6) 100%);
  }

  .portrait {
    position: absolute; left: 73px; top: 72px; width: 136px; height: 191px;
    background: linear-gradient(180deg, #b9bcbb 0%, #8f9492 60%, #6f7370 100%);
  }

  .identity { position: absolute; left: 226px; top: 96px; }
  .identity .name {
    font-family: "Encode Sans Semi Condensed", sans-serif; font-weight: 500;
    font-size: 20.5px; line-height: 24px; color: var(--brand-green);
  }
  .identity .role {
    font-family: "Encode Sans Semi Condensed", sans-serif; font-weight: 300;
    font-size: 14px; margin-top: 1px;
  }

  .contact { position: absolute; left: 226px; top: 174px; list-style: none; font-size: 15.5px; font-weight: 300; }
  .contact li { display: flex; align-items: center; height: 24.5px; }
  .contact svg { width: 16px; height: 16px; margin-right: 7px; flex: none; }

  .brand-mark {
    position: absolute; left: 560px; top: 82px; width: 216px;
    display: flex; align-items: center; gap: 9px;
  }
  .brand-mark .dot { width: 30px; height: 30px; border-radius: 50%; background: var(--brand-green); flex: none; }
  .brand-mark .brand-name {
    color: var(--brand-green); font-weight: 400; font-size: 19px; line-height: 23px;
  }

  .section-title {
    position: absolute; left: 73px; font-weight: 400; font-size: 24px; line-height: 30px; color: var(--brand-green);
  }
  .bio-title { top: 284px; }
  .clients-title { top: 570px; }
  .affiliations-title { top: 831px; }

  .bio {
    position: absolute; left: 73px; top: 325px; width: 680px;
    font-size: 15.6px; line-height: 21.6px;
  }
  .bio p { text-indent: 4px; }

  .plain-list { position: absolute; left: 73px; list-style: none; font-size: 15.6px; line-height: 21.6px; }
  .clients { top: 613px; }
  .affiliations { top: 874px; }
</style>
</head>
<body>
<main class="page">
  <div class="backdrop-wave" role="img" aria-label="Soft flowing green and lime wave lines along the bottom of the page"></div>

  <div class="portrait" role="img" aria-label="Head-and-shoulders portrait of the broker in a grey suit"></div>

  <header class="identity">
    <h1 class="name">R. Dalton Brinwell, CCAM, CLP</h1>
    <p class="role">Principal / Broker in Charge</p>
  </header>

  <ul class="contact">
    <li><svg viewBox="0 0 16 16"><path fill="var(--brand-green-dark)" d="M1 6c0-2 3-3.5 7-3.5S15 4 15 6v1.2h-3.2V5.6c-1-.4-2.4-.6-3.8-.6s-2.8.2-3.8.6v1.6H1zM4 7.5h8l2 3.5v3H2v-3z"/></svg>(555) 214-3080 ext. 114</li>
    <li><svg viewBox="0 0 16 16"><circle cx="8" cy="8" r="6.8" fill="none" stroke="var(--brand-green-dark)" stroke-width="1.3"/><path fill="var(--brand-green-dark)" d="M5.3 4.3l1.3-.3.9 2-.8.7c.4 1 1 1.7 2 2.2l.7-.8 2 .9-.3 1.4c-2.9.2-6-2.9-5.8-6.1z"/></svg>(555) 307-4492</li>
    <li><svg viewBox="0 0 16 16"><rect x="1.5" y="3.5" width="13" height="9" fill="none" stroke="var(--brand-green-dark)" stroke-width="1.3"/><path d="M1.5 3.5l6.5 5 6.5-5M1.5 12.5l5-4M14.5 12.5l-5-4" fill="none" stroke="var(--brand-green-dark)" stroke-width="1.1"/></svg>dalton@coltbrinwellre.com</li>
    <li><svg viewBox="0 0 16 16"><g fill="none" stroke="var(--brand-green-dark)" stroke-width="1.1"><circle cx="8" cy="8" r="6.5"/><ellipse cx="8" cy="8" rx="3" ry="6.5"/><path d="M1.5 8h13M2.5 5h11M2.5 11h11"/></g></svg>www.coltbrinwellre.com</li>
  </ul>

  <div class="brand-mark">
    <span class="dot"></span>
    <p class="brand-name">Colt Brinwell<br>Real Estate, LLC</p>
  </div>

  <h2 class="section-title bio-title">Bio</h2>
  <div class="bio">
    <p>Dalton began his real estate career in 2005 and has completed $75+ million in transactions representing sellers and buyers of commercial real estate, providing tenant representation, and leasing of retail and office properties. Prior to beginning his real estate career, Dalton served over five years in the Army Reserves and attended Harlow Ridge State University.</p>
    <p>Dalton has earned the prestigious Certified Commercial Advisory Member (CCAM) designation as well as the Certified Leasing Professional (CLP) designation. Dalton is a member of the National Guild of Retail Centers (NGRC), the Eastbay and Millbrook Realtor Association, the Millbrook County Chamber of Commerce, and serves on the board of directors for the Regional CCAM Chapter, the Sandhills Community Youth League, and the Tall Oak Realtors Association. Dalton is a licensed real estate broker in NC and SC.</p>
  </div>

  <h2 class="section-title clients-title">Clients Served</h2>
  <ul class="plain-list clients">
    <li>Cluckworth Kitchen</li>
    <li>Tallbridge Burgers</li>
    <li>Fairway Cuts</li>
    <li>Roadline Tire Co.</li>
    <li>Petit Crumb</li>
    <li>Brightway Home Health</li>
    <li>Kinward Services</li>
    <li>Corner Signal Marketing</li>
    <li>Ridgecrest Beverage Partners</li>
  </ul>

  <h2 class="section-title affiliations-title">Professional Affiliations</h2>
  <ul class="plain-list affiliations">
    <li>Certified Commercial Advisory Member (designee)</li>
    <li>National Guild of Retail Centers</li>
    <li>Tall Oak Realtors Association</li>
    <li>Regional Realtors Commercial Forms Committee</li>
  </ul>
</main>
</body>
</html>
```